Contractor Business Card Design

Looking to have a card made that has a bold description of (KITCHENS, BASEMENTS, BATHROOMS)

Definition and layers a plus

Contact info is;

Mark T. Ellery
Brookhaven, MN 55990
Cell: 612-555-0147
website: www.cobaltfinishworks.example
Email: cobaltfinishworksmn@mailbox.example

colors: red, black, gray, white

Contact Information for Business Card

Contact info is;

Mark T. Ellery
Brookhaven, MN 55990
Cell: 612-555-0147

Colors
ec1f27

Requirements
Must have
• Looking for layers and definition
Nice to have
• Cards are planned to be printed on plastic cards

```html
<!DOCTYPE html>
<html lang="en">
<head>
<meta charset="utf-8">
<title>Cobalt Finish Works – Business Card</title>
<link rel="stylesheet" href="https://fonts.googleapis.com/css2?family=PT+Sans+Narrow:wght@700&family=Open+Sans:wght@400;700&display=swap">
<style>
  :root {
    --stage: #d9d6d2;
    --card: #eeeff0;
    --card-edge: #d4d6d8;
    --band: #58595b;
    --band-dark: #4a4b4d;
    --ink: #2b2b2d;
    --ink-soft: #4d4e50;
    --white: #ffffff;
    --red: #ec1f27;
  }
  * { margin: 0; padding: 0; box-sizing: border-box; }
  html, body {
    width: 1200px; height: 1022px; overflow: hidden;
    background: var(--stage);
    font-family: "Open Sans", Arial, sans-serif;
  }
  .stage {
    width: 1200px; height: 1022px;
    display: flex; flex-direction: column; align-items: center; justify-content: center;
    gap: 40px;
  }
  .card {
    position: relative;
    width: 760px; height: 434px;
    background: var(--card);
    border: 1px solid var(--card-edge);
    border-radius: 6px;
    overflow: hidden;
    box-shadow: 0 10px 28px rgba(0,0,0,.18);
  }

  /* Front */
  .services-banner {
    position: absolute; left: 50%; top: 0; transform: translateX(-50%);
    width: 670px; height: 60px;
  }
  .services-banner svg { position: absolute; inset: 0; }
  .services-banner h2 {
    position: relative; line-height: 56px; text-align: center;
    font-family: "PT Sans Narrow", "Arial Narrow", sans-serif;
    font-weight: 700; font-size: 34px; letter-spacing: 1.2px;
    color: var(--white); white-space: nowrap;
  }
  .contact-block { position: absolute; left: 70px; top: 148px; }
  .contact-name {
    font-weight: 700; font-size: 29px; letter-spacing: .5px;
    color: var(--ink); text-transform: uppercase;
    margin-left: 44px; margin-bottom: 34px; white-space: nowrap;
  }
  .contact-line {
    display: flex; align-items: center; gap: 14px;
    font-size: 23px; color: var(--ink-soft); line-height: 34px; white-space: nowrap;
  }
  .contact-line .icon { width: 30px; height: 28px; display: flex; justify-content: center; }
  .brand-mark {
    position: absolute; right: 62px; top: 138px; width: 230px;
    display: flex; flex-direction: column; align-items: center; gap: 18px;
  }
  .brand-mark .dot {
    width: 92px; height: 92px; border-radius: 50%;
    border: 4px solid var(--red);
  }
  .brand-mark .brand-name {
    font-family: "Open Sans", Arial, sans-serif; font-weight: 700;
    font-size: 26px; line-height: 32px; letter-spacing: 2px;
    color: var(--ink); text-align: center; text-transform: uppercase;
  }
  .web-bar {
    position: absolute; left: 0; right: 0; bottom: 0; height: 46px;
    background: var(--band-dark);
    display: flex; align-items: center;
    color: var(--white); font-size: 18px; white-space: nowrap;
  }
  .web-bar .notch { position: absolute; top: -10px; }
  .web-item { display: flex; align-items: center; gap: 16px; }
  .web-item.site { margin-left: 18px; }
  .web-item.mail { margin-left: 22px; }

  /* Back */
  .back .band {
    position: absolute; left: 0; right: 0; height: 38px; background: var(--band);
  }
  .back .band.top { top: 0; }
  .back .band.bottom { bottom: 0; }
  .back .brand-mark { right: auto; left: 50%; top: 100px; transform: translateX(-50%); width: 600px; gap: 26px; }
  .back .brand-mark .dot { width: 120px; height: 120px; border-width: 5px; }
  .back .brand-mark .brand-name { font-size: 36px; line-height: 44px; white-space: nowrap; }
</style>
</head>
<body>
<main class="stage">

  <section class="card front" aria-label="Card front">
    <div class="services-banner">
      <svg width="670" height="60" viewBox="0 0 670 60" aria-hidden="true">
        <path d="M0 0 H670 L640 60 H30 Z" fill="var(--band)"/>
      </svg>
      <h2>KITCHENS, BASEMENTS, BATHROOMS</h2>
    </div>

    <div class="contact-block">
      <p class="contact-name">Mark T. Ellery</p>
      <p class="contact-line">
        <span class="icon">
          <svg width="28" height="26" viewBox="0 0 28 26" aria-hidden="true">
            <path d="M14 1 L27 13 H23 V25 H17 V17 H11 V25 H5 V13 H1 Z" fill="var(--ink-soft)"/>
          </svg>
        </span>
        Brookhaven, MN 55990
      </p>
      <p class="contact-line"><span class="icon"></span>Cell: 612-555-0147</p>
    </div>

    <div class="brand-mark">
      <span class="dot"></span>
      <p class="brand-name">Cobalt<br>Finish Works</p>
    </div>

    <footer class="web-bar">
      <svg class="notch" style="left:52px" width="20" height="10" viewBox="0 0 20 10" aria-hidden="true"><path d="M0 10 L10 0 L20 10 Z" fill="var(--band-dark)"/></svg>
      <svg class="notch" style="left:392px" width="20" height="10" viewBox="0 0 20 10" aria-hidden="true"><path d="M0 10 L10 0 L20 10 Z" fill="var(--band-dark)"/></svg>
      <div class="web-item site">
        <svg width="22" height="22" viewBox="0 0 22 22" aria-hidden="true">
          <g fill="none" stroke="var(--white)" stroke-width="1.6">
            <circle cx="11" cy="11" r="9.5"/><ellipse cx="11" cy="11" rx="4" ry="9.5"/>
            <path d="M1.5 11 H20.5 M3 6 H19 M3 16 H19"/>
          </g>
        </svg>
        <span>www.cobaltfinishworks.example</span>
      </div>
      <div class="web-item mail">
        <svg width="22" height="16" viewBox="0 0 22 16" aria-hidden="true">
          <rect x="1" y="1" width="20" height="14" fill="none" stroke="var(--white)" stroke-width="1.6"/>
          <path d="M1 1 L11 9 L21 1" fill="none" stroke="var(--white)" stroke-width="1.6"/>
        </svg>
        <span>cobaltfinishworksmn@mailbox.example</span>
      </div>
    </footer>
  </section>

  <section class="card back" aria-label="Card back">
    <div class="band top"></div>
    <div class="brand-mark">
      <span class="dot"></span>
      <p class="brand-name">Cobalt Finish Works</p>
    </div>
    <div class="band bottom"></div>
  </section>

</main>
</body>
</html>
```